Export company based in South America (Ecuador) we export flowers, chocolate, and bananas

We need a website that gives our potential clients and introduction into our company and the different types of commodities we export around the world. We are based in Quito, Ecuador so the website should portray the feel of Ecuadorian landscapes within a modern looking website.
At the moment we are exporting roses, chocolate, and bananas so the website should have an intro to our company and then three different areas that describe our three main commodity. The three different sections should explain why each of the products from Ecuador are some of the best in the world in their categories and the benefits of importing the commodity through our company.
Industry/Entity Type
Commodity
Number of Pages Required
4 page

```html
<!DOCTYPE html>
<html lang="en">
<head>
<meta charset="UTF-8">
<title>Andexa — Ecuadorian Exports</title>
<link href="https://fonts.googleapis.com/css2?family=Outfit:wght@300;400;500;600;700;800;900&display=swap" rel="stylesheet">
<style>
:root{
  --red:#fb3f5a;
  --blue:#1f5e9e;
  --ink:#1b1b1b;
  --text:#3a3a3a;
  --muted:#6b6b6b;
  --white:#ffffff;
  --footer:#232323;
  --line:#d9d9d9;
}
*{margin:0;padding:0;box-sizing:border-box}
html,body{width:1200px;height:3569px;overflow:hidden;background:var(--white)}
body{position:relative;font-family:"Outfit",sans-serif;color:var(--text)}
.abs{position:absolute}
a{color:inherit;text-decoration:none}

/* header */
.brand{font-weight:700;font-size:32px;color:var(--blue);display:flex;align-items:center;gap:10px}
.brand-dot{width:34px;height:34px;border-radius:50%;background:var(--blue)}
.site-header .brand{left:75px;top:28px}
.nav{display:flex;font-size:13.5px;color:var(--ink)}
.nav a{position:absolute;white-space:nowrap}
.site-header .nav{top:38px;left:0}
.nav-active-bar{left:438px;top:24px;width:36px;height:2px;background:var(--red)}
.search{left:964px;top:34px}
.quote-btn{left:1008px;top:28px;width:116px;height:36px;border-radius:18px;background:var(--red);color:#fff;font-weight:600;font-size:14px;display:flex;align-items:center;justify-content:center}

/* hero */
.hero-photo{left:0;top:96px;width:761px;height:592px;background:linear-gradient(135deg,#9a8a78 0%,#6a5240 40%,#4a3428 70%,#7a6a5e 100%)}
.slider-dots{top:607px;left:0}
.slider-dots span{position:absolute;top:0;width:12px;height:12px;border-radius:50%;border:2px solid #fff}
.slider-dots span.on{background:#fff}
.hero-badge{left:105px;top:647px;width:248px;height:81px;background:var(--red);border-radius:6px;color:#fff;display:flex;align-items:center}
.hero-badge .num{font-size:38px;font-weight:800;width:100px;text-align:center}
.hero-badge .sep{width:1px;height:52px;background:rgba(255,255,255,.6);margin-right:18px}
.hero-badge .label{font-size:13px;font-weight:300}
.hero-card{left:534px;top:190px;width:591px;height:563px;background:#fff;border-radius:44px 44px 150px 44px;box-shadow:0 18px 40px rgba(0,0,0,.1)}
.eyebrow{color:var(--red);font-size:25px;font-weight:400}
.hero-card .eyebrow{left:76px;top:92px}
.hero-title{left:76px;top:128px;font-size:60px;line-height:60px;font-weight:900;color:var(--ink)}
.hero-text{left:76px;top:276px;width:430px;font-size:13px;line-height:24px;font-weight:300}
.btn-outline{height:36px;padding:0 14px;border:1.5px solid var(--ink);border-radius:18px;font-weight:600;font-size:14px;color:var(--ink);display:inline-flex;align-items:center}
.btn-solid{height:36px;padding:0 14px;border-radius:18px;font-weight:600;font-size:14px;color:#fff;background:var(--red);display:inline-flex;align-items:center}
.cta{display:flex;align-items:center;gap:18px}
.hero-card .cta{left:76px;top:396px}

/* about */
.about-title{left:150px;top:862px;font-size:57px;font-weight:500;color:var(--ink)}
.about-text{left:150px;top:955px;width:450px;font-size:13px;line-height:24px;font-weight:300}
.about .cta{left:150px;top:1246px}
.about-divider{left:659px;top:859px;width:2px;height:416px;background:var(--line)}
.feature{left:718px;width:400px;height:130px}
.feature-icon{position:absolute;left:0;top:0;width:83px;height:83px;border-radius:50%;background:linear-gradient(135deg,#2a5fa8 0%,#7b4a8a 55%,#f0405a 100%);display:flex;align-items:center;justify-content:center}
.feature h3{position:absolute;left:102px;top:8px;font-size:31px;font-weight:400;color:var(--ink)}
.feature p{position:absolute;left:105px;top:54px;width:215px;font-size:11.5px;line-height:22px;font-weight:300}

/* products */
.products{left:0;top:1390px;width:1200px;height:839px;background:var(--red)}
.section-title{width:100%;text-align:center;font-size:56px;font-weight:600;color:#fff}
.products .section-title{top:94px}
.section-sub{width:100%;text-align:center;font-size:13px;line-height:24px;font-weight:300;color:#fff}
.products .section-sub{top:184px}
.product-card{top:294px;width:286px;height:416px;background:#fff;border-radius:10px 10px 56px 10px;text-align:center}
.product-photo{position:absolute;left:8px;top:8px;width:270px;height:154px}
.product-card h3{position:absolute;top:188px;width:100%;font-size:29px;font-weight:400;color:var(--ink)}
.product-card p{position:absolute;top:240px;left:38px;width:210px;font-size:11.5px;line-height:22px;font-weight:300}
.product-card .cta{position:absolute;left:58px;top:335px}

/* benefits */
.port-photo{left:0;top:2229px;width:1200px;height:429px;background:linear-gradient(180deg,#6f7a7e 0%,#4c6e82 45%,#2d4a5e 100%)}
.benefits{left:75px;top:2439px;width:1049px;height:679px;background:var(--blue);border-radius:56px 56px 120px 56px}
.benefits .section-title{top:78px;font-weight:600;font-size:58px}
.benefits .section-sub{top:184px}
.benefit{top:293px;width:186px;height:186px;border-radius:50%;border:1px solid rgba(255,255,255,.55);color:#fff;text-align:center}
.benefit-icon{position:absolute;left:10px;top:-6px;width:50px;height:46px;background:var(--blue);display:flex;align-items:center;justify-content:center}
.benefit h4{position:absolute;top:60px;width:100%;font-size:17px;font-weight:500}
.benefit p{position:absolute;top:92px;left:28px;width:130px;font-size:11.5px;line-height:22px;font-weight:300}
.benefits .cta{left:439px;top:534px}

/* newsletter */
.news-title{top:3198px;width:1200px;text-align:center;font-size:56px;font-weight:900;color:var(--ink)}
.news-sub{top:3290px;width:1200px;text-align:center;font-size:13px;color:var(--text);font-weight:300}
.news-form{left:387px;top:3343px;width:424px;height:48px;border-radius:24px;background:#fff;box-shadow:0 6px 20px rgba(0,0,0,.1)}
.news-form span{position:absolute;left:16px;top:15px;font-size:13px;color:#999}
.news-form b{position:absolute;right:6px;top:5px;width:122px;height:38px;border-radius:19px;background:var(--blue);color:#fff;font-size:10.5px;font-weight:700;display:flex;align-items:center;justify-content:center;letter-spacing:.3px}

/* footer */
.site-footer{left:0;top:3502px;width:1200px;height:67px;background:var(--footer)}
.site-footer .brand{left:75px;top:18px;font-size:23px;color:#fff;gap:8px}
.site-footer .brand-dot{width:26px;height:26px;background:#fff}
.site-footer .nav{color:#fff;top:26px}
.socials span{position:absolute;top:21px;width:26px;height:26px;border-radius:50%}
</style>
</head>
<body>

<header class="site-header">
  <div class="abs brand"><span class="brand-dot"></span>Andexa</div>
  <div class="abs nav-active-bar"></div>
  <nav class="abs nav">
    <a style="left:438px">Home</a><a style="left:498px">About</a><a style="left:560px">Services</a><a style="left:633px">Blogs</a><a style="left:692px">Contact Us</a>
  </nav>
  <svg class="abs search" width="26" height="26" viewBox="0 0 26 26" fill="none" stroke="#1b1b1b" stroke-width="2.4" stroke-linecap="round"><circle cx="11" cy="11" r="8"/><path d="M17 17l6 6"/></svg>
  <a class="abs quote-btn">Get A Quote</a>
</header>

<section class="hero">
  <div class="abs hero-photo" role="img" aria-label="Hands holding a heap of cocoa beans"></div>
  <div class="abs slider-dots"><span style="left:149px"></span><span class="on" style="left:223px"></span><span class="on" style="left:295px"></span></div>
  <div class="abs hero-badge"><span class="num">01</span><span class="sep"></span><span class="label">Cocoa Beans</span></div>
  <div class="abs hero-card">
    <p class="abs eyebrow">We Export</p>
    <h1 class="abs hero-title">Around The<br>World</h1>
    <p class="abs hero-text">Lorem Ipsum Is Simply Dummy Text Of The Printing And Typesetting Industry. Lorem Ipsum Has Been The Industry's Standard Dummy Text Ever Since The 1500s, When</p>
    <div class="abs cta"><a class="btn-outline">Explore More</a><svg width="34" height="12" viewBox="0 0 34 12" fill="none" stroke="#1b1b1b" stroke-width="1.6"><path d="M0 6h32M27 1l5 5-5 5"/></svg></div>
  </div>
</section>

<section class="about">
  <h2 class="abs about-title">About Us</h2>
  <p class="abs about-text">Lorem Ipsum Is Simply Dummy Text Of The Printing And Typesetting Industry. Lorem Ipsum Has Been The Industry's Standard Dummy Text Ever Since The 1500s, When An Unknown Printer Took A Galley Of Type And Scrambled It To Make A Type Specimen Book. It Has Survived Not Only Five Centuries, But Also The Leap Into Electronic Typesetting, Remaining Essentially Unchanged. It Was Popularised In The 1960s With The Release Of Pressline Sheets Containing Lorem Ipsum Passages, And More Recently With Desktop Publishing Software Like Quillset Layout Including Versions Of Lorem Ipsum.</p>
  <div class="abs cta"><a class="btn-solid">Explore More</a><svg width="34" height="12" viewBox="0 0 34 12" fill="none" stroke="#1b1b1b" stroke-width="1.6"><path d="M0 6h32M27 1l5 5-5 5"/></svg></div>
  <div class="abs about-divider"></div>

  <div class="abs feature" style="top:860px">
    <div class="feature-icon"><svg width="40" height="40" viewBox="0 0 40 40" fill="none" stroke="#fff" stroke-width="1.6"><circle cx="20" cy="17" r="12"/><circle cx="20" cy="17" r="7"/><path d="M20 13l1.3 2.6 2.8.4-2 2 .5 2.8-2.6-1.4-2.6 1.4.5-2.8-2-2 2.8-.4z"/><path d="M13 27l-3 9 5-2 3 4 2-8M27 27l3 9-5-2-3 4-2-8"/></svg></div>
    <h3>Quality</h3>
    <p>Lorem Ipsum Is Simply Dummy Text Of The Printing And Typesetting Industry. Lorem Ipsum</p>
  </div>
  <div class="abs feature" style="top:1004px">
    <div class="feature-icon"><svg width="40" height="40" viewBox="0 0 40 40" fill="none" stroke="#fff" stroke-width="1.6"><circle cx="22" cy="23" r="12"/><path d="M22 17v6l4 3M19 7h6M22 7v4M4 19h7M6 24h5M8 29h4"/></svg></div>
    <h3>Quickness</h3>
    <p>Lorem Ipsum Is Simply Dummy Text Of The Printing And Typesetting Industry. Lorem Ipsum</p>
  </div>
  <div class="abs feature" style="top:1148px">
    <div class="feature-icon"><svg width="40" height="40" viewBox="0 0 40 40" fill="none" stroke="#fff" stroke-width="1.6"><path d="M30 20V7H8v26h14"/><path d="M12 13h2M17 13h9M12 19h2M17 19h9M12 25h2M17 25h5"/><circle cx="28" cy="28" r="5"/><path d="M32 32l4 4"/></svg></div>
    <h3>Result</h3>
    <p>Lorem Ipsum Is Simply Dummy Text Of The Printing And Typesetting Industry. Lorem Ipsum</p>
  </div>
</section>

<section class="abs products">
  <h2 class="abs section-title">Our Products</h2>
  <p class="abs section-sub">Lorem Ipsum Is Simply Dummy Text Of The Printing And Typesetting Industry. Lorem Ipsum Has Been The<br>Industry's Standard Dummy Text Ever Since The 1500s, When</p>

  <article class="abs product-card" style="left:150px">
    <div class="product-photo" role="img" aria-label="Boxes of red roses packed for export" style="background:linear-gradient(180deg,#3a5aa0 0%,#d8313a 35%,#e23a3a 65%,#3a4e8c 100%)"></div>
    <h3>Roses</h3>
    <p>Lorem Ipsum Is Simply Dummy Text Of The Printing And Typesetting Industry. Lorem Ipsum</p>
    <div class="cta"><a class="btn-outline">Explore More</a><svg width="34" height="12" viewBox="0 0 34 12" fill="none" stroke="#1b1b1b" stroke-width="1.6"><path d="M0 6h32M27 1l5 5-5 5"/></svg></div>
  </article>
  <article class="abs product-card" style="left:457px">
    <div class="product-photo" role="img" aria-label="Sack of cocoa beans with a metal scoop" style="background:radial-gradient(ellipse at 50% 60%,#b06a55 0%,#8a5a44 40%,#4a3a2c 80%,#1e1a16 100%)"></div>
    <h3>Chocolate</h3>
    <p>Lorem Ipsum Is Simply Dummy Text Of The Printing And Typesetting Industry. Lorem Ipsum</p>
    <div class="cta"><a class="btn-outline">Explore More</a><svg width="34" height="12" viewBox="0 0 34 12" fill="none" stroke="#1b1b1b" stroke-width="1.6"><path d="M0 6h32M27 1l5 5-5 5"/></svg></div>
  </article>
  <article class="abs product-card" style="left:764px">
    <div class="product-photo" role="img" aria-label="Market stall piled with ripe bananas" style="background:linear-gradient(180deg,#5a5040 0%,#b8a04a 40%,#d8c060 70%,#8a7a3a 100%)"></div>
    <h3>Bananas</h3>
    <p>Lorem Ipsum Is Simply Dummy Text Of The Printing And Typesetting Industry. Lorem Ipsum</p>
    <div class="cta"><a class="btn-outline">Explore More</a><svg width="34" height="12" viewBox="0 0 34 12" fill="none" stroke="#1b1b1b" stroke-width="1.6"><path d="M0 6h32M27 1l5 5-5 5"/></svg></div>
  </article>
</section>

<div class="abs port-photo" role="img" aria-label="Aerial view of a container port with cranes and stacked containers"></div>

<section class="abs benefits">
  <h2 class="abs section-title">Benefits</h2>
  <p class="abs section-sub">Lorem Ipsum Dolor Sit Amet, Consectetur Adipiscing Elit, Sed Do Eiusmod Tempor Incididunt Ut Labore Et<br>Dolore Magna Aliqua. Ut Enim Ad Minim Veniam, Quis Nostrud Exercitation Ullamco</p>

  <div class="abs benefit" style="left:94px">
    <div class="benefit-icon"><svg width="34" height="38" viewBox="0 0 34 38" fill="none" stroke="#fff" stroke-width="1.6"><path d="M17 2l13 5v11c0 9-6 15-13 18C10 33 4 27 4 18V7z"/><circle cx="17" cy="19" r="7"/><path d="M14 19l2 2 4-4"/></svg></div>
    <h4>Safe Ingredients</h4>
    <p>Lorem Ipsum Dolor Sit Amet, Consectetur Adipiscing Elit,</p>
  </div>
  <div class="abs benefit" style="left:316px">
    <div class="benefit-icon"><svg width="40" height="38" viewBox="0 0 40 38" fill="none" stroke="#fff" stroke-width="1.6"><path d="M2 30h8l8 4h10l10-6-2-2-9 4h-7M10 30v-6h6l6 3h5"/><path d="M24 20v-8M24 14c-5 0-6-4-6-6 4 0 6 2 6 6zM24 12c0-4 3-6 7-6 0 3-2 6-7 6z"/></svg></div>
    <h4>Eco Friendly</h4>
    <p>Lorem Ipsum Dolor Sit Amet, Consectetur Adipiscing Elit,</p>
  </div>
  <div class="abs benefit" style="left:539px">
    <div class="benefit-icon"><svg width="32" height="38" viewBox="0 0 32 38" fill="none" stroke="#fff" stroke-width="1.6"><path d="M4 2h18l6 6v28H4z"/><path d="M8 10h12M8 16h4v4H8zM15 18h9M8 24h4v4H8zM15 26h9"/></svg></div>
    <h4>100% Tested</h4>
    <p>Lorem Ipsum Dolor Sit Amet, Consectetur Adipiscing Elit,</p>
  </div>
  <div class="abs benefit" style="left:763px">
    <div class="benefit-icon"><svg width="40" height="38" viewBox="0 0 40 38" fill="none" stroke="#fff" stroke-width="1.6"><circle cx="20" cy="19" r="4"/><ellipse cx="20" cy="9" rx="5" ry="7"/><ellipse cx="20" cy="29" rx="5" ry="7"/><ellipse cx="10" cy="19" rx="7" ry="5"/><ellipse cx="30" cy="19" rx="7" ry="5"/></svg></div>
    <h4>Natural Based</h4>
    <p>Lorem Ipsum Dolor Sit Amet, Consectetur Adipiscing Elit,</p>
  </div>

  <div class="abs cta"><a class="btn-solid">Explore More</a><svg width="34" height="12" viewBox="0 0 34 12" fill="none" stroke="#fff" stroke-width="1.6"><path d="M0 6h32M27 1l5 5-5 5"/></svg></div>
</section>

<section class="newsletter">
  <h2 class="abs news-title">Subscribe To Our Newsletter</h2>
  <p class="abs news-sub">Continually Productize Business Scenarios Through Transparent Niches. Synergistically Impact Web-Enabled</p>
  <div class="abs news-form"><span>Email</span><b>SUBSCRIBE</b></div>
</section>

<footer class="abs site-footer">
  <div class="abs brand"><span class="brand-dot"></span>Andexa</div>
  <nav class="abs nav">
    <a style="left:438px">Home</a><a style="left:498px">About</a><a style="left:560px">Services</a><a style="left:633px">Blogs</a><a style="left:692px">Contact Us</a>
  </nav>
  <div class="socials">
    <span style="left:982px;background:#3b5ba8"></span>
    <span style="left:1021px;background:#2fa4e6"></span>
    <span style="left:1060px;background:#d1308f"></span>
    <span style="left:1098px;background:#1c76b8"></span>
  </div>
</footer>

</body>
</html>
```